Elegant, High End Integrated Wellness Healthcare Practice

We need a brochure designed for an integrated mind-body wellness healthcare practice (www.larkfernclinic.com) . This brochure will be used when we cold call prospects (physicians to refer to our office, and potential consumers to utilize our services). Our practice is geographically located in the middle Tennessee USA region, although we have plans to become an international company as many of our offerings can be accessed anywhere in the world. Ultimately our goal is to have this brochure used as a leave-behind in an effort to introduce our integrated offerings to increase market share. The final product brochure should be both elegant and serious, with clean lines but also convey warmth and trust, as individuals who are coming for our services have usually struggled with their health for a significant amount of time before finding our practice.
Updates

The design brief was very specific about providing a high-end science-based 2-page brochure (not flier). Several designs submitted were fliers. The other designs were heavy on yoga or "woo woo" non-science-based looking pictures. This is a flier to appeal to physicians and other healthcare providers. Therefore the design must speak science and evidence-based methods of mind and body wellness care. I would also like to appeal to the other designers I paid extra for their submissions and who have indicated they will "respond in the coming days."

```html
<!DOCTYPE html>
<html lang="en">
<head>
<meta charset="utf-8">
<title>Larkfern Clinic Brochure</title>
<link rel="stylesheet" href="https://fonts.googleapis.com/css2?family=Cinzel:wght@400;600;700&family=Open+Sans:ital,wght@0,400;0,600;0,700;1,400&display=swap">
<style>
  :root{
    --forest:#344f25;
    --forest-deep:#22361a;
    --lime:#8cc63f;
    --lime-light:#b5dc6d;
    --navy:#0f1a3d;
    --paper:#ffffff;
    --backdrop:#e6e7e8;
    --ink:#2b3a22;
    --muted:#5b6655;
  }
  *{box-sizing:border-box;margin:0;padding:0}
  html,body{width:1098px;height:1200px;overflow:hidden}
  body{background:var(--backdrop);font-family:"Open Sans",Arial,sans-serif;position:relative}
  .spread{position:absolute;left:149px;width:800px;height:540px;display:flex;box-shadow:0 6px 20px rgba(0,0,0,.25)}
  .spread--outer{top:30px}
  .spread--inner{top:620px}
  .page{position:relative;width:400px;height:540px;overflow:hidden;background:var(--paper)}
  .page__art{position:absolute;inset:0;width:100%;height:100%}

  /* back cover */
  .testimonial{position:absolute;left:30px;width:340px;border:1.5px solid rgba(255,255,255,.8);border-radius:10px;padding:16px 22px 14px;color:#fff}
  .testimonial__quote{font-size:10.5px;font-style:italic;line-height:1.5}
  .testimonial__name{margin-top:6px;font-size:10.5px;font-weight:700;color:var(--lime)}
  .testimonial__mark{position:absolute;height:18px;font-family:Georgia,serif;font-size:32px;font-weight:700;color:var(--lime);line-height:.9;background:var(--forest);padding:0 4px;overflow:hidden}
  .testimonial__mark--open{top:-9px;left:12px}
  .testimonial__mark--close{bottom:-9px;right:12px}
  .brand{position:absolute;display:flex;align-items:center;gap:8px}
  .brand__dot{width:34px;height:34px;border-radius:50%;background:var(--forest)}
  .brand__name{font-family:"Cinzel",Georgia,serif;font-weight:600;font-size:16px;line-height:1.1;color:var(--forest)}
  .brand--back{left:236px;top:446px}
  .contact{position:absolute;left:26px;top:456px;font-size:8.5px;font-weight:600;line-height:1.5;color:var(--ink)}
  .url{position:absolute;left:0;right:0;text-align:center;font-weight:700;letter-spacing:1px;color:var(--forest-deep)}
  .url--back{top:511px;font-size:13px;color:#fff}
  .url--front{top:511px;font-size:12px}

  /* front cover */
  .brand--front{left:118px;top:24px}
  .brand--front .brand__dot{background:#fff;width:40px;height:40px}
  .brand--front .brand__name{color:#fff;font-size:18px}
  .headline{position:absolute;left:0;right:0;top:388px;text-align:center;font-family:"Cinzel",Georgia,serif;font-weight:600;line-height:1.15}
  .headline__lead{display:block;color:#fff;font-size:23px}
  .headline__accent{display:block;color:var(--lime);font-size:31px}

  /* inner spread */
  .tab{position:absolute;left:0;top:74px;width:212px;height:40px;background:var(--lime);clip-path:polygon(0 0,100% 0,88% 100%,0 100%);font-family:"Cinzel",Georgia,serif;font-weight:600;font-size:22px;color:#fff;padding:6px 0 0 22px;white-space:nowrap}
  .intro{position:absolute;left:22px;right:22px;top:20px;color:#fff}
  .intro__title{font-family:"Cinzel",Georgia,serif;font-weight:600;font-size:13px;line-height:1.25;margin-bottom:7px}
  .intro__text{font-size:7.4px;line-height:1.5}
  .services{position:absolute;display:grid;gap:8px 7px}
  .services--left{left:26px;top:126px;grid-template-columns:repeat(4,80px)}
  .services--right{left:20px;top:214px;grid-template-columns:repeat(5,66px);gap:10px 7px}
  .service{background:#fff;box-shadow:0 1px 4px rgba(0,0,0,.25);display:flex;flex-direction:column}
  .service__photo{height:68px}
  .services--right .service__photo{height:64px}
  .service__label{height:22px;background:var(--lime);display:flex;align-items:center;justify-content:center;text-align:center;font-size:6.4px;font-weight:700;line-height:1.1;text-transform:uppercase;color:var(--forest-deep);padding:0 3px}
  .tone-a{background:linear-gradient(135deg,#d9c7a8,#8a6a4a)}
  .tone-b{background:linear-gradient(135deg,#c9dfe9,#5a7f8f)}
  .tone-c{background:linear-gradient(135deg,#e8d6c2,#b88a6a)}
  .tone-d{background:linear-gradient(135deg,#2a3f7a,#0c1433)}
  .tone-e{background:linear-gradient(135deg,#b9c9a2,#5b7340)}
  .tone-f{background:linear-gradient(135deg,#f0c48a,#b0663a)}
  .tone-g{background:linear-gradient(135deg,#e6e9ee,#9aa4b0)}
</style>
</head>
<body>

<section class="spread spread--outer">
  <article class="page page--back">
    <svg class="page__art" viewBox="0 0 400 540" preserveAspectRatio="none" aria-hidden="true">
      <path d="M0 0H400V392C300 424 150 442 0 428Z" fill="var(--forest)"/>
      <path d="M0 428C150 442 300 424 400 392V406C300 438 150 456 0 442Z" fill="var(--lime)"/>
      <rect x="0" y="500" width="400" height="40" fill="var(--lime)"/>
    </svg>
    <div class="testimonial" style="top:20px">
      <span class="testimonial__mark testimonial__mark--open">&ldquo;</span>
      <p class="testimonial__quote">I wish I could give them 100 stars. Dr. Avery and his staff have been such a blessing in my life. With their help I am having such a wonderful life.</p>
      <p class="testimonial__name">Nora Whitlock</p>
    </div>
    <div class="testimonial" style="top:134px">
      <p class="testimonial__quote">Doctor Elena Park is an extremely talented and effective counselor. Her care includes several additional helps for clients. I have worked on food and exercise issues with her, and my stress, anxiety and depression have truly benefited. We are so glad to have found this clinic; it has been a life changing path for all of us.</p>
      <p class="testimonial__name">Glen Harwood</p>
      <span class="testimonial__mark testimonial__mark--close">&rdquo;</span>
    </div>
    <div class="testimonial" style="top:296px">
      <span class="testimonial__mark testimonial__mark--open">&ldquo;</span>
      <p class="testimonial__quote">These people are an absolute pleasure to work with! I'd give them a 10 star rating if I could!</p>
      <p class="testimonial__name">R.</p>
      <span class="testimonial__mark testimonial__mark--close">&rdquo;</span>
    </div>
    <div class="brand brand--back">
      <span class="brand__dot"></span>
      <span class="brand__name">Larkfern<br>Clinic</span>
    </div>
    <p class="contact">418 Birchwood Ln. Alder Springs, TN 37000<br>Office Hours: Monday - Friday: 8 am - 7 pm<br>Call Now or Appointment Requests</p>
    <p class="url url--back">www.larkfernclinic.com</p>
  </article>

  <article class="page page--front" style="background:var(--navy)">
    <svg class="page__art" viewBox="0 0 400 540" preserveAspectRatio="none" aria-hidden="true">
      <defs>
        <linearGradient id="frontBand" x1="0" x2="0" y1="0" y2="1">
          <stop offset="0" stop-color="var(--forest)"/>
          <stop offset="1" stop-color="var(--forest-deep)"/>
        </linearGradient>
      </defs>
      <path d="M0 330C120 300 260 300 400 290V540H0Z" fill="url(#frontBand)"/>
      <path d="M0 318C120 288 260 288 400 278V292C260 302 120 302 0 332Z" fill="var(--lime)"/>
      <rect x="0" y="500" width="400" height="40" fill="var(--lime-light)"/>
    </svg>
    <div role="img" aria-label="Photo of a glowing digital brain over a tablet beside herbs, ginger and remedy bottles" style="position:absolute;left:0;top:92px;width:400px;height:212px;background:linear-gradient(100deg,#1b2f6b 0%,#3d5c9c 40%,#d8d2c4 65%,#a88a62 100%);clip-path:polygon(0 0,100% 0,100% 88%,0 100%)"></div>
    <div class="brand brand--front">
      <span class="brand__dot"></span>
      <span class="brand__name">Larkfern<br>Clinic</span>
    </div>
    <h1 class="headline">
      <span class="headline__lead">Discover a Better Way</span>
      <span class="headline__accent">To a Better You</span>
    </h1>
    <p class="url url--front">www.larkfernclinic.com</p>
  </article>
</section>

<section class="spread spread--inner">
  <article class="page page--services">
    <svg class="page__art" viewBox="0 0 400 540" preserveAspectRatio="none" aria-hidden="true">
      <path d="M0 0H400V150C250 170 120 178 0 172Z" fill="var(--forest)"/>
    </svg>
    <h2 class="tab">Our Services</h2>
    <div class="services services--left">
      <div class="service"><div class="service__photo tone-b" role="img" aria-label="Illustration of colourful head profiles"></div><p class="service__label">Social Brain Care</p></div>
      <div class="service"><div class="service__photo tone-e" role="img" aria-label="Illustrated tree diagram of functional medicine"></div><p class="service__label">Functional Medicine</p></div>
      <div class="service"><div class="service__photo tone-c" role="img" aria-label="Photo of a healthy meal and exercise"></div><p class="service__label">Healthy Lifestyle Package</p></div>
      <div class="service"><div class="service__photo tone-d" role="img" aria-label="Photo of a light therapy panel"></div><p class="service__label">Light Therapy for Pain</p></div>
      <div class="service"><div class="service__photo tone-a" role="img" aria-label="Photo of hands holding a small plant"></div><p class="service__label">Wellness Package</p></div>
      <div class="service"><div class="service__photo tone-g" role="img" aria-label="Illustration of a brain with colourful icons"></div><p class="service__label">Mind Health</p></div>
      <div class="service"><div class="service__photo tone-e" role="img" aria-label="Photo of a couple walking outdoors"></div><p class="service__label">Body Health</p></div>
      <div class="service"><div class="service__photo tone-g" role="img" aria-label="Photo of a person resting"></div><p class="service__label">Sleep Restoration</p></div>
      <div class="service"><div class="service__photo tone-f" role="img" aria-label="Photo of people sitting at sunset"></div><p class="service__label">Stress Management</p></div>
      <div class="service"><div class="service__photo tone-d" role="img" aria-label="Illustration of a digital body scan"></div><p class="service__label">Body Composition Scan</p></div>
      <div class="service"><div class="service__photo tone-b" role="img" aria-label="Photo of laboratory test tubes"></div><p class="service__label">Lab Testing</p></div>
      <div class="service"><div class="service__photo tone-g" role="img" aria-label="Photo of a worried person"></div><p class="service__label">Anxiety Treatment</p></div>
      <div class="service"><div class="service__photo tone-g" role="img" aria-label="Photo of a person meditating"></div><p class="service__label">Meditation</p></div>
      <div class="service"><div class="service__photo tone-c" role="img" aria-label="Photo of a back with highlighted pain area"></div><p class="service__label">Fibromyalgia</p></div>
      <div class="service"><div class="service__photo tone-f" role="img" aria-label="Photo of a shoulder with highlighted inflammation"></div><p class="service__label">Inflammation &amp; Body Pain</p></div>
      <div class="service"><div class="service__photo tone-b" role="img" aria-label="Illustration of steps leading to a target"></div><p class="service__label">SFBT</p></div>
    </div>
  </article>

  <article class="page page--intro">
    <svg class="page__art" viewBox="0 0 400 540" preserveAspectRatio="none" aria-hidden="true">
      <path d="M0 0H400V176C280 184 140 190 0 192Z" fill="var(--forest)"/>
    </svg>
    <div class="intro">
      <h3 class="intro__title">Wellness Services Offered at Larkfern Clinic in Alder Springs, TN</h3>
      <p class="intro__text">At Larkfern Clinic we facilitate body and mind health and wellness through an integrated functional approach to care. This method of personalized care appreciates you as a unique individual with distinct health circumstances. We tailor our body and mind approaches to address your specific health concerns. Through the combination of body and mind interventions, we address concerns such as attention deficit, distractibility and learning concerns, chronic pain and inflammation conditions, and psychiatric conditions such as anxiety, depression, panic, and many more. The result is integrative healing-oriented care that addresses every aspect of your whole person: body, mind, and spirit. For a free confidential consultation call us today or book a consultation online. We are conveniently located at 418 Birchwood Ln. Alder Springs, TN 37000.</p>
    </div>
    <div class="services services--right">
      <div class="service"><div class="service__photo tone-f" role="img" aria-label="Photo of a person stretching at sunrise"></div><p class="service__label">Whole Body Wellness</p></div>
      <div class="service"><div class="service__photo tone-g" role="img" aria-label="Photo of a prescription pad with vegetables"></div><p class="service__label">Nutritional Wellness</p></div>
      <div class="service"><div class="service__photo tone-a" role="img" aria-label="Photo of a person resting outdoors"></div><p class="service__label">360° Integrated Wellness</p></div>
      <div class="service"><div class="service__photo tone-d" role="img" aria-label="Photo of a glowing brain above a tablet"></div><p class="service__label">Brain Wave Mapping</p></div>
      <div class="service"><div class="service__photo tone-c" role="img" aria-label="Photo of a person holding their head"></div><p class="service__label">ADHD</p></div>
      <div class="service"><div class="service__photo tone-g" role="img" aria-label="Photo of an eye movement therapy session"></div><p class="service__label">EMDR</p></div>
      <div class="service"><div class="service__photo tone-b" role="img" aria-label="Photo of a person in distress"></div><p class="service__label">Depression</p></div>
      <div class="service"><div class="service__photo tone-e" role="img" aria-label="Photo of vegetables and a meal plan"></div><p class="service__label">Nutritional Coach</p></div>
      <div class="service"><div class="service__photo tone-g" role="img" aria-label="Photo of a book about healing from trauma"></div><p class="service__label">PTSD</p></div>
      <div class="service"><div class="service__photo tone-f" role="img" aria-label="Photo of a person with raised arms at sunset"></div><p class="service__label">Emotional Freedom Technique</p></div>
      <div class="service"><div class="service__photo tone-b" role="img" aria-label="Photo of a breath analysis mask"></div><p class="service__label">Breath Analysis</p></div>
      <div class="service"><div class="service__photo tone-g" role="img" aria-label="Photo of a clinician with supplements"></div><p class="service__label">Nutraceuticals</p></div>
      <div class="service"><div class="service__photo tone-d" role="img" aria-label="Illustration of a glowing stomach"></div><p class="service__label">GERD</p></div>
      <div class="service"><div class="service__photo tone-c" role="img" aria-label="Photo of a person with chest discomfort"></div><p class="service__label">Heartburn</p></div>
      <div class="service"><div class="service__photo tone-a" role="img" aria-label="Photo of hands holding a model of the gut"></div><p class="service__label">IBS</p></div>
    </div>
  </article>
</section>

</body>
</html>
```